Business Card for Pottery and Jewellery Designer

A new business card design is needed to accompany a newly launching pottery and jewellery website. The company logo has been attached for use. The company is called Glazewick Studio. For a sense of the vibe please see the website (it is currently under construction but this way you'll get a feel for the style) www.GlazewickStudio.com

The website font is Pontano Sans for the body of the text with Overlock for headers.

The overall look should be clean and elegant. The back side can have just the logo. The front side should have a smaller logo and the following details displayed:

Glazewick Studio
Designer: Hollis Marrow
Phone: xxx.xxx.xxxx
Email: Designer@GlazewickStudio.com

The structure of displaying this is completely up to you. Different layouts and creative methods of displaying contact info are welcome as long as it stays clean/uncluttered.

No product photographs are to be included in the design as the catalogue changes quickly.

Colour preferences lean towards elegant and understated (charcoal grey, dark navy blue etc.)

Please let me know if you have any further questions or further details required.

Target Market(s)

Target market is 30+ year old women

Industry/Entity Type

Construction

Colors
ffffff
1b1b1b
474747
d9d9d9
fafafa
0355a3

Requirements
Must have
• The submissions so far have looked very typical and don't stand out right now. They're also all in navy with very little variation. I'm looking for something that stands out a it more while still being clean-looking.
Nice to have
• I've attached a few design samples and an idea for a backdrop. It would be great to see some designs in black, white, and grey with only a hint of color.
Should not have
• Product Images

```html
<!DOCTYPE html>
<html lang="en">
<head>
<meta charset="utf-8">
<title>Glazewick Studio – Business Card</title>
<link rel="stylesheet" href="https://fonts.googleapis.com/css2?family=Overlock:wght@400;700&family=Open+Sans:wght@400;700&display=swap">
<style>
  :root {
    --backdrop: #ececec;
    --card: #f7f7f8;
    --accent: #231766;
    --charcoal: #474747;
    --ink: #1b1b1b;
    --white: #ffffff;
  }
  html, body {
    margin: 0;
    width: 1200px;
    height: 970px;
    overflow: hidden;
    background: var(--backdrop);
  }
  .canvas {
    position: relative;
    width: 1200px;
    height: 970px;
  }
  .card {
    position: absolute;
    left: 250px;
    width: 700px;
    height: 400px;
    background: var(--card);
    box-shadow: 0 6px 18px rgba(0,0,0,0.12);
    overflow: hidden;
  }
  .card--front { top: 70px; }
  .card--back { top: 500px; }

  .wave { position: absolute; inset: 0; width: 700px; height: 400px; }

  .brand {
    position: absolute;
    display: flex;
    align-items: center;
    gap: 22px;
  }
  .brand__mark {
    border-radius: 50%;
    background: var(--accent);
    flex: none;
  }
  .brand__name {
    font-family: "Overlock", sans-serif;
    font-weight: 400;
    color: var(--ink);
    text-transform: uppercase;
    letter-spacing: 1px;
    white-space: nowrap;
  }
  .card--front .brand { left: 40px; top: 30px; }
  .card--front .brand__mark { width: 46px; height: 46px; }
  .card--front .brand__name { font-size: 44px; }

  .contact {
    position: absolute;
    left: 44px;
    top: 110px;
    margin: 0;
    padding: 0;
    list-style: none;
    font-family: "Open Sans", sans-serif;
    font-size: 17px;
    color: var(--ink);
  }
  .contact__item {
    display: flex;
    align-items: center;
    gap: 14px;
    height: 25px;
  }
  .contact__icon { width: 15px; height: 15px; fill: var(--charcoal); flex: none; }

  .person {
    position: absolute;
    right: 34px;
    bottom: 14px;
    text-align right;
    text-align: right;
    font-family: "Open Sans", sans-serif;
    color: var(--white);
  }
  .person__name { font-size: 21px; font-weight: 700; line-height: 1.2; }
  .person__role { font-size: 16px; line-height: 1.3; }

  .card--back .brand {
    left: 0;
    right: 0;
    top: 155px;
    justify-content: center;
  }
  .card--back .brand__mark { width: 90px; height: 90px; order: 2; }
  .card--back .brand__name { font-size: 50px; }
</style>
</head>
<body>
<main class="canvas">

  <section class="card card--front" aria-label="Card front">
    <svg class="wave" viewBox="0 0 700 400" aria-hidden="true">
      <path d="M0,204 C170,272 420,306 700,322 C430,313 190,282 0,228 Z" fill="var(--accent)"/>
      <path d="M0,244 C180,302 390,328 700,338 L700,400 L0,400 Z" fill="var(--charcoal)"/>
    </svg>

    <div class="brand">
      <span class="brand__mark"></span>
      <span class="brand__name">Glazewick Studio</span>
    </div>

    <ul class="contact">
      <li class="contact__item">
        <svg class="contact__icon" viewBox="0 0 16 16" aria-hidden="true"><path d="M3 2h3l1 3-2 1c1 2 2 3 4 4l1-2 3 1v3c0 1-1 2-2 2C6 14 2 10 2 4c0-1 0-2 1-2z"/></svg>
        <span>1234.555.019</span>
      </li>
      <li class="contact__item">
        <svg class="contact__icon" viewBox="0 0 16 16" aria-hidden="true"><path d="M1 3h14v10H1z M2 4l6 5 6-5"/></svg>
        <span>designer@glazewickstudio.com</span>
      </li>
      <li class="contact__item">
        <svg class="contact__icon" viewBox="0 0 16 16" aria-hidden="true"><circle cx="8" cy="8" r="7"/></svg>
        <span>www.glazewickstudio.com</span>
      </li>
    </ul>

    <div class="person">
      <div class="person__name">Hollis Marrow</div>
      <div class="person__role">Designer</div>
    </div>
  </section>

  <section class="card card--back" aria-label="Card back">
    <div class="brand">
      <span class="brand__mark"></span>
      <span class="brand__name">Glazewick Studio</span>
    </div>
  </section>

</main>
</body>
</html>
```